Podcast Cover Design - Tiding For Level Heads

We renamed our podcast from the "Harborline Property Hour Podcast" to "Tidings For Level Heads" and we need a new podcast cover design, Instagram profile picture, and a YouTube banner.

More so we're looking for some sort of symbol/icon. Our old logo had the Cobalt Spire but we're moving to a much broader audience that isn't necessarily from Seattle and needs something that will appeal to them.

In the podcast, Doran reads the news that big media isn't covering including crime, business, homeless crisis, protests. We stay away from covering politics but our audience is mainly right-wing.

Attached are some additional designs we created in-house.

If we love the design we'll have additional job opportunities to create possible designs for merchandise.

Target Market(s)

80% Males aged 50+, Republican

Industry/Entity Type

News

Colors

Designer to choose colors to be used in the design.

Requirements
Must have
• OPEN TOO IDEAS
Nice to have
• OPEN TOO IDEAS
Should not have
• Cobalt Spire

```html
<!DOCTYPE html>
<html lang="en">
<head>
<meta charset="utf-8">
<title>Tidings For Level Heads – Podcast Cover</title>
<link rel="stylesheet" href="https://fonts.googleapis.com/css2?family=Anton&family=Montserrat:wght@300;800&display=swap">
<style>
  :root {
    --paper: #ffffff;
    --harbor-blue: #0e5c7e;
    --signal-red: #dc3334;
    --host-warm: #b5746a;
    --host-deep: #5a2b3a;
  }
  html, body {
    margin: 0;
    padding: 0;
    width: 1200px;
    height: 1200px;
    overflow: hidden;
    background: var(--paper);
  }
  .cover {
    position: relative;
    width: 1200px;
    height: 1200px;
    background: var(--paper);
  }
  .cover__panel {
    position: absolute;
    left: 48px;
    top: 50px;
    width: 1104px;
    height: 1096px;
    background: var(--harbor-blue);
    overflow: hidden;
  }
  .cover__backdrop {
    position: absolute;
    left: -48px;
    top: -50px;
    width: 1200px;
    height: 1200px;
  }
  .host-photo {
    position: absolute;
    left: 0;
    top: 592px;
    width: 680px;
    height: 504px;
    border-radius: 320px 320px 0 0 / 260px 260px 0 0;
    background: linear-gradient(180deg, var(--host-warm) 0%, #a8605e 55%, var(--host-deep) 100%);
  }
  .cover__type {
    position: absolute;
    left: 0;
    top: 0;
    width: 1200px;
    height: 1200px;
  }
  .title-word {
    font-family: "Anton", "Oswald", sans-serif;
  }
  .title-small,
  .host-name {
    font-family: "Montserrat", "Helvetica", sans-serif;
    font-weight: 800;
  }
  .host-label {
    font-family: "Montserrat", "Helvetica", sans-serif;
    font-weight: 300;
  }
</style>
</head>
<body>
<main class="cover">
  <section class="cover__panel">
    <svg class="cover__backdrop" viewBox="0 0 1200 1200" aria-hidden="true">
      <path d="M0,945 L48,935 C250,790 570,800 748,1146 L748,1300 L0,1300 Z"
            fill="var(--signal-red)" stroke="var(--paper)" stroke-width="4"/>
    </svg>
    <div class="host-photo" role="img" aria-label="Portrait photo of host Doran Holloway beside a vintage studio microphone"></div>
  </section>

  <svg class="cover__type" viewBox="0 0 1200 1200" role="img" aria-label="Tidings For Level Heads, with host Doran Holloway">
    <text class="title-word" x="134" y="335" font-size="214" fill="var(--paper)"
          textLength="463" lengthAdjust="spacingAndGlyphs">TIDINGS</text>
    <text class="title-small" x="625" y="212" font-size="80" fill="var(--paper)"
          textLength="167" lengthAdjust="spacingAndGlyphs">FOR</text>
    <text class="title-word" x="625" y="338" font-size="124" fill="var(--signal-red)"
          textLength="441" lengthAdjust="spacingAndGlyphs">LEVEL</text>
    <text class="title-word" x="137" y="632" font-size="310" fill="var(--signal-red)"
          stroke="var(--paper)" stroke-width="3" paint-order="stroke"
          textLength="929" lengthAdjust="spacingAndGlyphs">HEADS</text>

    <g class="mic-icon" fill="none" stroke="var(--paper)" stroke-width="9" stroke-linecap="round">
      <rect x="795" y="738" width="40" height="72" rx="20" fill="var(--paper)" stroke="none"/>
      <path d="M791,808 Q791,846 815,846 Q839,846 839,808"/>
      <line x1="815" y1="846" x2="815" y2="862"/>
      <line x1="799" y1="862" x2="831" y2="862"/>
      <path d="M781,760 Q769,782 781,806"/>
      <path d="M849,760 Q861,782 849,806"/>
      <path d="M765,742 Q743,784 765,828"/>
      <path d="M865,742 Q887,784 865,828"/>
    </g>

    <text class="host-label" x="751" y="925" font-size="52" fill="var(--paper)"
          textLength="292" lengthAdjust="spacingAndGlyphs">WITH HOST</text>
    <text class="host-name" x="751" y="997" font-size="62" fill="var(--paper)">DORAN</text>
    <text class="host-name" x="751" y="1048" font-size="62" fill="var(--paper)"
          textLength="320" lengthAdjust="spacingAndGlyphs">HOLLOWAY</text>
  </svg>
</main>
</body>
</html>
```